New Record Label needs a Web design

We are Iron Heron: a London based, new & independent music production company aimed at the 25-40 age group. The musical style is Soul/Classic Brelvane.
We have at the moment just one signed artist, but will expand in the future.
We dont' have any webpage yet and are looking for an innovative web design for our webpage www.iron-heron-example.com
I have uploaded our company logo.

Initially the whole website will only have 3 tabs: Home page/Artists/Contact

The design should be classic and high-end, but can be a bit crazy too.

```html
<!DOCTYPE html>
<html lang="en">
<head>
<meta charset="utf-8">
<title>Iron Heron — Music Production</title>
<link href="https://fonts.googleapis.com/css2?family=Bebas+Neue&family=Montserrat:wght@500&family=Arimo:wght@400;700&display=swap" rel="stylesheet">
<style>
:root{
  --ink:#13131c;
  --cream:#f3ecd9;
  --cream-btn:#f5eedc;
  --brown:#4a2a1c;
  --orange:#f26c3a;
  --red:#e8453a;
  --red-border:#f0735a;
  --nav-light:#e8dccb;
  --white:#fff8ec;
}
*{margin:0;padding:0;box-sizing:border-box}
html,body{width:846px;height:1200px;overflow:hidden;background:var(--ink)}
body{position:relative;font-family:'Arimo',Arial,sans-serif}
.abs{position:absolute}
.display{font-family:'Bebas Neue',Impact,sans-serif;font-weight:400;line-height:1}

.site-header{top:0;left:0;width:846px;height:78px;background:var(--ink)}
.brand{left:80px;top:26px;display:flex;align-items:center;gap:6px;color:var(--red);font-family:'Bebas Neue',Impact,sans-serif;font-size:22px}
.brand-dot{width:14px;height:14px;border-radius:50%;background:var(--red)}
.main-nav{left:219px;top:29px;display:flex;gap:24px;font-size:19px}
.main-nav a{color:var(--orange);text-decoration:none}
.main-nav a.current{color:var(--nav-light)}
.social{left:640px;top:33px;display:flex;gap:6px}
.social span{width:16px;height:16px;border-radius:50%;background:var(--red);display:block}

.hero{top:78px;left:0;width:846px;height:195px;background:linear-gradient(160deg,#d9cdb4 0%,#6e6252 35%,#2b2620 60%,#8a7a63 85%,#3a312a 100%)}

.services{top:273px;left:0;width:846px;height:332px;background:var(--cream)}
.service{position:absolute;width:240px}
.service svg{position:absolute;left:-44px;top:0}
.service h2{font-size:38px;color:var(--brown);letter-spacing:.2px}
.service p{font-size:10px;line-height:12px;color:var(--brown);margin-top:2px}

.about{top:605px;left:0;width:846px;height:393px;background:var(--orange)}
.section-title{font-size:46px;color:var(--white)}
.who{left:114px;top:68px;width:292px}
.who p{font-size:10px;line-height:12px;color:var(--white);margin-top:22px}
.who p+p{margin-top:20px}
.read-more{display:inline-block;margin-top:22px;margin-left:-2px;width:86px;height:22px;line-height:22px;text-align:center;background:var(--cream-btn);color:var(--orange);font-size:10px;text-decoration:none}
.artists{left:445px;top:68px;width:290px}
.artist-list{margin-top:2px}
.artist{display:flex;height:65px;margin-bottom:2px;background:var(--red);border:1px solid var(--red-border)}
.artist-photo{width:86px;height:63px;flex:none}
.artist-body{padding:12px 12px 0 10px}
.artist h3{font-family:'Montserrat',Arial,sans-serif;font-weight:500;font-size:12px;color:var(--white);text-transform:uppercase}
.artist p{font-size:8px;line-height:10px;color:var(--white);margin-top:3px}

.site-footer{top:998px;left:0;width:846px;height:202px;background:var(--ink)}
.footer-brand{left:108px;top:76px}
.footer-brand .brand-name{display:flex;align-items:center;gap:6px;color:var(--red);font-family:'Bebas Neue',Impact,sans-serif;font-size:22px}
.footer-brand small{display:block;margin-top:14px;font-size:8px;color:var(--orange)}
.footer-title{font-size:34px;color:var(--nav-light)}
.footer-nav{left:256px;top:62px}
.footer-links{display:grid;grid-template-columns:58px 60px;margin-top:1px;margin-left:2px;font-size:10px;line-height:12px}
.footer-links a{color:var(--orange);text-decoration:none}
.connect{left:448px;top:62px;width:300px}
.connect p{font-size:11px;color:var(--orange);margin-top:1px;margin-left:2px}
.connect p b{font-weight:700}
.signup{display:flex;margin-top:6px;margin-left:2px}
.signup .field{width:222px;height:22px;background:var(--orange)}
.signup .button{margin-left:6px;width:68px;height:22px;line-height:22px;text-align:center;background:var(--red);color:var(--white);font-size:10px}
</style>
</head>
<body>

<header class="site-header abs">
  <div class="brand abs"><span class="brand-dot"></span>Iron Heron</div>
  <nav class="main-nav abs display">
    <a class="current" href="#">Home</a><a href="#">Studio</a><a href="#">Artists</a><a href="#">Contact</a>
  </nav>
  <div class="social abs" aria-label="Social links"><span></span><span></span><span></span><span></span><span></span></div>
</header>

<div class="hero abs" role="img" aria-label="Close-up photo of studio headphones resting on a mixing console"></div>

<section class="services abs">
  <div class="service" style="left:160px;top:60px">
    <svg width="26" height="46" viewBox="0 0 26 46"><rect x="7" y="2" width="12" height="24" rx="6" fill="#e8453a"/><path d="M3 20a10 10 0 0 0 20 0" fill="none" stroke="#e8453a" stroke-width="2.5"/><rect x="12" y="30" width="2.5" height="10" fill="#e8453a"/><rect x="6" y="40" width="14" height="3" fill="#e8453a"/></svg>
    <h2 class="display">Recording</h2>
    <p>Lorem ipsum dolor sit amet conse ctetur adipisicing elit, sed do eiusmod tempor incididunt ut labore et dolore magna aliqua.</p>
  </div>
  <div class="service" style="left:487px;top:60px">
    <svg width="36" height="42" viewBox="0 0 36 42"><g fill="#e8453a"><rect x="4" y="2" width="3" height="38"/><rect x="16" y="2" width="3" height="38"/><rect x="28" y="2" width="3" height="38"/></g><g fill="#f3ecd9" stroke="#e8453a" stroke-width="2"><rect x="1" y="20" width="9" height="6"/><rect x="13" y="28" width="9" height="6"/><rect x="25" y="12" width="9" height="6"/></g></svg>
    <h2 class="display">Mixing</h2>
    <p>Mes cuml dia sed in lacus ut eniascetertu ingerto aliiqt es siteta eismod ictordol uteto ligula ameti dapibus ticdu mtsent lusto dolor ltisi commes.</p>
  </div>
  <div class="service" style="left:160px;top:206px">
    <svg width="36" height="36" viewBox="0 0 36 36"><circle cx="18" cy="18" r="17" fill="#e8453a"/><circle cx="18" cy="18" r="9" fill="#f3ecd9"/><circle cx="18" cy="18" r="3.5" fill="none" stroke="#e8453a" stroke-width="1"/></svg>
    <h2 class="display">Mastering</h2>
    <p>Lorem ipsum dolor sit amet conse ctetur adipisicing elit, sed do eiusmod tempor incididunt ut labore et dolore magna aliqua.</p>
  </div>
  <div class="service" style="left:487px;top:206px">
    <svg width="36" height="40" viewBox="0 0 36 40"><path d="M12 6 L34 2 V28" fill="none" stroke="#e8453a" stroke-width="4"/><path d="M12 6 V32" stroke="#e8453a" stroke-width="4"/><ellipse cx="7" cy="32" rx="6" ry="5" fill="#e8453a"/><ellipse cx="29" cy="28" rx="6" ry="5" fill="#e8453a"/></svg>
    <h2 class="display">Sound System</h2>
    <p>Mes cuml dia sed in lacus ut eniascetertu ingerto aliiqt es siteta eismod ictordol uteto ligula ameti dapibus ticdu mtsent lusto dolor ltisi commes.</p>
  </div>
</section>

<section class="about abs">
  <div class="who abs">
    <h2 class="section-title display">Who We Are</h2>
    <p>Lorem ipsum dolor sit amet conse ctetur adipisicing elit, sed do eiusmod tempor incididunt ut labore et dolore magna aliqua. Ut enim ad minim veniam quis nostrud</p>
    <p>Sit amet conse ctetur adipisicing elit, sed do eiusmod tempor incididunt ut labore et dolore magna aliqua. Ut enim ad minim veniam, quis nostrud exercitation ullamco laboris nisi ut aliquip ex ea commodo consequat. Duis aute irure dolor in reprehenderit in voluptate velit esse cillum dolore eu fugiat nulla pariatur. Excepteur sint occaecat cupidatat non proident, sunt in culpa qui officia deserunt.</p>
    <a class="read-more" href="#">read more</a>
  </div>
  <div class="artists abs">
    <h2 class="section-title display">Artists</h2>
    <div class="artist-list">
      <article class="artist">
        <div class="artist-photo" role="img" aria-label="Portrait photo of a singer wearing red headphones" style="background:linear-gradient(135deg,#3a4a66,#e8c9b8 60%,#c0304a)"></div>
        <div class="artist-body"><h3>Lira Montaval</h3><p>Over 3 hours of cruising through the NYC harbor. Enjoy the open-air deck and admire.</p></div>
      </article>
      <article class="artist">
        <div class="artist-photo" role="img" aria-label="Band photo outdoors in front of a stone tower" style="background:linear-gradient(160deg,#3d7ad0,#8aa070 55%,#3f6a2e)"></div>
        <div class="artist-body"><h3>Copper Lantern</h3><p>Arrive on the pier and walk down the red carpet with your group. A team of professional .</p></div>
      </article>
      <article class="artist">
        <div class="artist-photo" role="img" aria-label="Band members posing against a dark wall" style="background:linear-gradient(160deg,#4a4a48,#1f1f1f 60%,#6a6a60)"></div>
        <div class="artist-body"><h3>Bright Tessel Band</h3><p>Hit the floor and enjoy hophop DJ Orvello's spin sessions. With millions of light combinations</p></div>
      </article>
    </div>
  </div>
</section>

<footer class="site-footer abs">
  <div class="footer-brand abs">
    <div class="brand-name"><span class="brand-dot"></span>Iron Heron</div>
    <small>Copyright © 2014</small>
  </div>
  <div class="footer-nav abs">
    <h2 class="footer-title display">Navigation</h2>
    <div class="footer-links"><a href="#">Home</a><a href="#">Songs</a><a href="#">Artists</a><a href="#">Contact</a></div>
  </div>
  <div class="connect abs">
    <h2 class="footer-title display">Connect with Iron Heron</h2>
    <p><b>subscribe</b> to our newsletter</p>
    <div class="signup"><div class="field"></div><div class="button">Subscribe</div></div>
  </div>
</footer>

</body>
</html>
```